Dr. Marisa Tellen Medical/Chiropractic Business Card

Dr. Tellen is a chiropractor and will require a business card that she uses every single day to book appointments on the back side of the card. Currently the office name goes by Dr. Marisa Tellen. The chiropractic profession is based on the diagnosis and manipulative treatment of misalignments of the joints, especially those of the spinal column, which are held to cause other disorders by affecting the nerves, muscles, and organs. Dr. Marisa Tellen is looking for a contemporary and minimalistic design.

Industry/Entity Type

Medical

Contact Information for Business Card

Name: Dr. Marisa Tellen; Address: 748 Ashcombe Rd North, London, ON N5R 2K9; Phone Number: 519.672.4193; Fax: 519.681.2054; email: marisa.tellen@brevanmail.com

Requirements
Must have
• ability to write multiple appointments date/time on the back of card

```html
<!DOCTYPE html>
<html lang="en">
<head>
<meta charset="utf-8">
<title>Dr. Marisa Tellen – Business &amp; Appointment Card</title>
<link rel="stylesheet" href="https://fonts.googleapis.com/css2?family=Ubuntu:wght@500&family=Questrial&family=Roboto+Condensed:wght@400;700&display=swap">
<style>
  :root {
    --purple: #4a0f9a;
    --purple-deep: #3a0a80;
    --purple-light: #5a1fb0;
    --lavender: #a88cc8;
    --lavender-soft: #c9b6e0;
    --paper: #ffffff;
    --ink: #3c3c3c;
    --rule: #8a8a8a;
    --backdrop: #ecebef;
  }
  * { margin: 0; padding: 0; box-sizing: border-box; }
  html, body { width: 1200px; height: 800px; overflow: hidden; }
  body { background: var(--backdrop); position: relative; }

  .card {
    position: absolute;
    background: var(--paper);
    border-radius: 12px;
    overflow: hidden;
    box-shadow: 0 2px 10px rgba(0,0,0,0.12);
  }

  /* Business card front */
  .business-card { left: 60px; top: 223px; width: 620px; height: 354px; }
  .business-card .side-band { position: absolute; inset: 0; }
  .identity {
    position: absolute; left: 62px; top: 66px;
    display: flex; align-items: center; gap: 16px;
  }
  .identity-mark {
    width: 20px; height: 20px; border-radius: 50%;
    background: var(--purple);
  }
  .identity-name {
    font-family: "Ubuntu", sans-serif; font-weight: 500;
    font-size: 36px; color: var(--purple); letter-spacing: -0.5px; line-height: 1;
  }
  .identity-title {
    position: absolute; left: 98px; top: 110px;
    font-family: "Questrial", sans-serif; font-size: 19px; color: var(--ink);
  }
  .contact-list {
    position: absolute; left: 64px; top: 215px; list-style: none;
    font-family: "Questrial", sans-serif; font-size: 15px; color: var(--ink);
  }
  .contact-list li { display: flex; align-items: center; gap: 10px; height: 20px; }
  .contact-icon {
    width: 15px; height: 15px; border-radius: 3px; background: var(--purple);
    display: block;
  }
  .address {
    position: absolute; left: 66px; top: 288px;
    font-family: "Questrial", sans-serif; font-size: 15px; line-height: 23px; color: var(--ink);
  }

  /* Appointment card back */
  .appointment-card { left: 800px; top: 111px; width: 330px; height: 578px; }
  .appointment-header {
    height: 74px; background: linear-gradient(90deg, var(--purple-deep), var(--purple-light));
    display: flex; align-items: center; justify-content: center;
    font-family: "Roboto Condensed", sans-serif; font-weight: 700;
    font-size: 32px; color: #fff; letter-spacing: 0.5px;
  }
  .appointment-rows { list-style: none; padding: 22px 28px 0; }
  .appointment-row {
    display: flex; align-items: flex-end; height: 40px;
    font-family: "Roboto Condensed", sans-serif; font-size: 13px; color: var(--ink);
  }
  .appointment-row .slot-date { flex: 0 0 150px; border-bottom: 1px solid var(--rule); height: 1px; }
  .appointment-row .slot-at { padding: 0 3px; line-height: 1; }
  .appointment-row .slot-time { flex: 1; border-bottom: 1px solid var(--rule); height: 1px; }
  .cancellation-note {
    position: absolute; left: 0; right: 0; bottom: 34px; text-align: center;
    font-family: "Roboto Condensed", sans-serif; font-size: 16px; line-height: 20px; color: var(--ink);
  }
</style>
</head>
<body>

<section class="card business-card" aria-label="Business card front">
  <svg class="side-band" width="620" height="354" viewBox="0 0 620 354">
    <defs>
      <linearGradient id="band-fill" x1="0" y1="0" x2="0" y2="1">
        <stop offset="0" stop-color="#5a1fb0"/>
        <stop offset="1" stop-color="#3a0a80"/>
      </linearGradient>
      <linearGradient id="spine-fill" x1="0" y1="0" x2="1" y2="0">
        <stop offset="0" stop-color="#c9b6e0"/>
        <stop offset="1" stop-color="#a88cc8"/>
      </linearGradient>
    </defs>
    <path role="img" aria-label="Stylised spine column decoration"
          d="M448,0 L518,0 C490,120 475,230 468,354 L392,354 C398,230 418,120 448,0 Z"
          fill="url(#spine-fill)"/>
    <path d="M522,0 L620,0 L620,354 L472,354 C478,230 494,120 522,0 Z" fill="url(#band-fill)"/>
  </svg>

  <div class="identity">
    <span class="identity-mark"></span>
    <span class="identity-name">Dr. Marisa Tellen</span>
  </div>
  <p class="identity-title">Chiropractor</p>

  <ul class="contact-list">
    <li>
      <svg class="contact-icon" viewBox="0 0 15 15" aria-label="Phone"><rect width="15" height="15" rx="3" fill="#4a0f9a"/><path d="M4.5 3.5c.6-.4 1.1-.3 1.4.2l.7 1.2c.2.4 0 .8-.3 1l-.5.3c.4 1 1.1 1.8 2 2.3l.4-.5c.3-.3.7-.4 1-.2l1.2.7c.5.3.5.9.1 1.4-.8.9-2 .9-3 .3C5.7 9.3 4.3 7.6 3.8 5.6c-.2-.8 0-1.6.7-2.1z" fill="#fff"/></svg>
      519.672.4193
    </li>
    <li>
      <svg class="contact-icon" viewBox="0 0 15 15" aria-label="Fax"><rect width="15" height="15" rx="3" fill="#4a0f9a"/><rect x="5" y="3" width="5" height="3" fill="#fff"/><rect x="3.5" y="6.5" width="8" height="4" rx="1" fill="#fff"/><rect x="5" y="9.5" width="5" height="2.5" fill="#fff" stroke="#4a0f9a" stroke-width="0.6"/></svg>
      519.681.2054
    </li>
    <li>
      <svg class="contact-icon" viewBox="0 0 15 15" aria-label="Email"><rect width="15" height="15" rx="3" fill="#4a0f9a"/><rect x="3" y="4.5" width="9" height="6" fill="#fff"/><path d="M3 4.5l4.5 3.5 4.5-3.5" fill="none" stroke="#4a0f9a" stroke-width="0.8"/></svg>
      marisa.tellen@brevanmail.com
    </li>
  </ul>

  <p class="address">748 Ashcombe Rd North<br>London, ON N5R 2K9</p>
</section>

<section class="card appointment-card" aria-label="Appointment card back">
  <header class="appointment-header">APPOINTMENT CARD</header>
  <ul class="appointment-rows">
    <li class="appointment-row"><span class="slot-date"></span><span class="slot-at">@</span><span class="slot-time"></span></li>
    <li class="appointment-row"><span class="slot-date"></span><span class="slot-at">@</span><span class="slot-time"></span></li>
    <li class="appointment-row"><span class="slot-date"></span><span class="slot-at">@</span><span class="slot-time"></span></li>
    <li class="appointment-row"><span class="slot-date"></span><span class="slot-at">@</span><span class="slot-time"></span></li>
    <li class="appointment-row"><span class="slot-date"></span><span class="slot-at">@</span><span class="slot-time"></span></li>
    <li class="appointment-row"><span class="slot-date"></span><span class="slot-at">@</span><span class="slot-time"></span></li>
    <li class="appointment-row"><span class="slot-date"></span><span class="slot-at">@</span><span class="slot-time"></span></li>
    <li class="appointment-row"><span class="slot-date"></span><span class="slot-at">@</span><span class="slot-time"></span></li>
    <li class="appointment-row"><span class="slot-date"></span><span class="slot-at">@</span><span class="slot-time"></span></li>
  </ul>
  <p class="cancellation-note">If you are unable to make your appointment<br>please give 24 hours notice<br>by calling 519-672-4193</p>
</section>

</body>
</html>
```